Diesel injection diagnostics and repairs

I am after a business card design for my business.
The business; repairs diesel fuel systems on 4wds, trucks, earthmoving equipment,can do mobile repairs and diagnostics
The business design can basic but effective, I guess some colours such as green and black or even blue......
The end result should reflect the business name and logo and what the business can do

Industry/Entity Type

Business

Contact Information for Business Card

BW Diesel Injection PTY LTD
bw_diesel@trovamail.net
Dennis Holt
0491570156

```html
<!DOCTYPE html>
<html lang="en">
<head>
<meta charset="utf-8">
<title>BW Diesel Injection PTY LTD – Business Card</title>
<link href="https://fonts.googleapis.com/css2?family=Open+Sans:wght@400;600;700&display=swap" rel="stylesheet">
<style>
  :root {
    --page-bg: #e9e9ea;
    --kraft: #b3a490;
    --kraft-edge: #a39480;
    --ink: #1f1f1f;
    --ink-soft: #2b2b2b;
    --line: #3a3a3a;
    --mark: #8b7c68;
  }
  * { box-sizing: border-box; margin: 0; padding: 0; }
  html, body {
    width: 1200px; height: 648px; overflow: hidden;
    background: var(--page-bg);
    font-family: "Open Sans", Arial, sans-serif;
    color: var(--ink);
  }
  .sheet {
    position: relative; width: 1200px; height: 648px;
    display: flex; align-items: center; justify-content: center; gap: 60px;
  }
  .card {
    position: relative; width: 525px; height: 300px;
    background: var(--kraft);
    box-shadow: 0 10px 28px rgba(0,0,0,0.18), 0 0 0 1px var(--kraft-edge) inset;
    overflow: hidden;
  }

  /* Front */
  .brand-block {
    position: absolute; left: 30px; top: 30px;
    display: flex; align-items: center; gap: 10px;
  }
  .brand-block__square {
    width: 22px; height: 22px; background: var(--ink-soft);
  }
  .brand-block__name {
    font-weight: 700; font-size: 18px; color: var(--ink-soft);
  }
  .front__company {
    position: absolute; right: 30px; top: 98px; text-align: right;
    font-weight: 700; font-size: 22px; letter-spacing: -0.2px;
  }
  .front__services {
    position: absolute; right: 30px; top: 130px; text-align: right;
    font-weight: 600; font-size: 14px; line-height: 1.35;
  }
  .front__person {
    position: absolute; left: 30px; bottom: 68px;
    font-weight: 700; font-size: 24px;
  }
  .front__contact {
    position: absolute; right: 30px; bottom: 24px; text-align: right;
    font-size: 14px; line-height: 1.5; letter-spacing: 0.3px;
  }

  /* Back */
  .back__rule-h {
    position: absolute; left: 20px; right: 30px; top: 78px;
    height: 4px; background: var(--line);
  }
  .back__rule-v {
    position: absolute; left: 50px; top: 14px;
    width: 4px; height: 74px; background: var(--line);
  }
  .back__company {
    position: absolute; left: 66px; top: 26px;
    font-weight: 700; font-size: 27px; letter-spacing: -0.3px;
  }
  .back__web {
    position: absolute; left: 0; right: 0; top: 170px; text-align: center;
    font-size: 15px; letter-spacing: 0.3px;
  }
</style>
</head>
<body>
<main class="sheet">
  <section class="card card--front" aria-label="Business card front">
    <div class="brand-block">
      <span class="brand-block__square" aria-hidden="true"></span>
      <span class="brand-block__name">BW Diesel</span>
    </div>
    <h1 class="front__company">BW Diesel Injection PTY LTD</h1>
    <p class="front__services">repairs diesel fuel systems on 4wds<br>mobile repairs and diagnostics</p>
    <p class="front__person">Dennis Holt</p>
    <p class="front__contact">bw_diesel@trovamail.net<br>0491570156</p>
  </section>

  <section class="card card--back" aria-label="Business card back">
    <span class="back__rule-v" aria-hidden="true"></span>
    <span class="back__rule-h" aria-hidden="true"></span>
    <h2 class="back__company">BW Diesel Injection PTY LTD</h2>
    <p class="back__web">www.bwdieselworks.net</p>
  </section>
</main>
</body>
</html>
```